Natural Cosmetics need a Packaging Design

We need a PACKAGING design for labels on hand/body wash bottles and soap paper boxes.
We target at high end markets.
We expect a contemporary and trendy design.
We don't need a separate logo. The brand name "Ma Vitrine" acts as the logo.
We want a modern and classic font for "Ma Vitrine".
Please see attached pictures for packaging samples.

Industry/Entity Type

Cosmetics

Requirements
Should not have
• a separate logo from the brand name

```html
<!DOCTYPE html>
<html lang="en">
<head>
<meta charset="utf-8">
<title>Ma Vitrine – Body Wash Label</title>
<link rel="stylesheet" href="https://fonts.googleapis.com/css2?family=Amatic+SC:wght@400;700&display=swap">
<style>
  :root {
    --page-bg: #f4f6f3;
    --label-bg: #ffffff;
    --ink: #2f4a2b;
    --ink-soft: #6f7a6c;
    --rule: #9aa896;
  }
  * { margin: 0; padding: 0; box-sizing: border-box; }
  html, body {
    width: 1042px;
    height: 1200px;
    overflow: hidden;
    background: var(--page-bg);
  }
  .canvas {
    position: relative;
    width: 1042px;
    height: 1200px;
    display: flex;
    align-items: center;
    justify-content: center;
  }
  .label {
    position: relative;
    width: 392px;
    height: 1040px;
    background: var(--label-bg);
    color: var(--ink);
    font-family: "Amatic SC", cursive;
    box-shadow: 0 2px 14px rgba(40, 60, 40, 0.08);
  }
  .brand {
    position: absolute;
    top: 200px;
    left: 0;
    width: 100%;
    display: flex;
    align-items: center;
    justify-content: center;
    gap: 12px;
  }
  .brand-name {
    font-size: 58px;
    font-weight: 700;
    line-height: 1;
    color: var(--ink);
  }
  .brand-dot {
    width: 12px;
    height: 12px;
    border-radius: 50%;
    background: var(--ink);
  }
  .product-type {
    position: absolute;
    top: 470px;
    left: 24px;
    font-size: 96px;
    font-weight: 700;
    line-height: 1;
    letter-spacing: 1px;
  }
  .product-line {
    position: absolute;
    top: 592px;
    left: 24px;
    font-size: 90px;
    font-weight: 400;
    line-height: 1;
    letter-spacing: 2px;
  }
  .tagline {
    position: absolute;
    top: 708px;
    left: 26px;
    font-size: 42px;
    font-weight: 700;
    line-height: 1;
  }
  .claims {
    position: absolute;
    top: 782px;
    left: 18px;
    display: flex;
    gap: 18px;
    list-style: none;
    font-size: 27px;
    font-weight: 700;
    line-height: 1;
  }
  .claims li::before { content: "*"; font-size: 20px; vertical-align: top; margin-right: 1px; }
  .natural-seal {
    position: absolute;
    top: 862px;
    left: 236px;
    width: 130px;
    height: 120px;
  }
  .natural-seal text {
    font-family: "Amatic SC", cursive;
    fill: var(--ink);
  }
  .net-content {
    position: absolute;
    top: 990px;
    left: 30px;
    font-size: 20px;
    font-weight: 400;
    color: var(--ink-soft);
    letter-spacing: 1px;
  }
</style>
</head>
<body>
  <main class="canvas">
    <section class="label">
      <div class="brand">
        <span class="brand-name">Ma Vitrine</span>
        <span class="brand-dot"></span>
      </div>

      <h1 class="product-type">BODY WASH</h1>
      <p class="product-line">ORGANIC</p>
      <p class="tagline">FOOD FOR HEALTHY SKINY</p>

      <ul class="claims">
        <li>CHEMICAL FREE</li>
        <li>CRUELTY FREE</li>
        <li>CONSERN FREE</li>
      </ul>

      <svg class="natural-seal" viewBox="0 0 130 120" aria-label="100% natural">
        <path d="M22 30 A52 52 0 1 0 112 40" fill="none" stroke="var(--ink)" stroke-width="2" stroke-linecap="round"/>
        <text x="28" y="52" font-size="44" font-weight="700" transform="rotate(-14 60 50)">100%</text>
        <text x="30" y="88" font-size="34" font-weight="400" transform="rotate(-14 60 80)">NATURAL</text>
      </svg>

      <p class="net-content">NET 250 ML &nbsp;/&nbsp; 8 FL OZ</p>
    </section>
  </main>
</body>
</html>
```